Letterhead & Business Card for our Professional Practice (Financial Services)

We are looking for someone to design a letterhead and business card for our business, which is a professional practice called Harbor Lumen Capital Limited. The website is at www.harborrlumencapital.example.co.uk.

The letterhead needs to have: (a) our logo (b) address (c) telephone number (d) email address and (e) our company number.

We would like the stationary to be consistent with the website.

I have attached the logo in EPS and PNG format.

Target Market(s)

Professional services, large commercial enterprises, financial services

Industry/Entity Type

Financial Service

Font styles to use
Serif

Colors
3176b5
f04a50

Requirements
Must have
• Be consistent with our website located at www.harborlumencapital.example.co.uk
• Be in the following formats:
• 1. Word template for the letterhead
• 2. PDF for the letterhead with setup and bleeds required at www.presskite.example.co.uk
• 3. PDF for the business card with setup and bleeds required at www.presskite.example.co.uk
Nice to have
• Something with a really interesting design that says "these guys are professional but dynamic and interesting"
Should not have
• Boring

```html
<!DOCTYPE html>
<html lang="en">
<head>
<meta charset="utf-8">
<title>Harbor Lumen Capital – Letterhead</title>
<link rel="stylesheet" href="https://fonts.googleapis.com/css2?family=Alegreya+Sans:wght@500&family=Arimo:wght@400&family=Sarabun:wght@300&display=swap">
<style>
  :root {
    --brand-blue: #0a2a8f;
    --brand-red: #d4000f;
    --rule-blue: #6f86cf;
    --ink: #1a1a1a;
    --footer-text: #dfe5ff;
    --sig-tone: #e6e6e6;
  }
  * { margin: 0; padding: 0; box-sizing: border-box; }
  html, body { width: 927px; height: 1200px; overflow: hidden; background: #fff; }
  .letterhead { position: relative; width: 927px; height: 1200px; overflow: hidden; background: #fff; }
  .top-band { position: absolute; top: 0; left: 0; width: 100%; height: 6px; background: var(--brand-blue); }
  .brand { position: absolute; top: 44px; left: 0; width: 100%; text-align: center; }
  .brand-mark { display: block; width: 102px; height: 102px; margin: 0 auto 12px; background: var(--brand-red); }
  .brand-name {
    font-family: "Alegreya Sans", sans-serif; font-weight: 500; font-size: 44px;
    color: var(--brand-blue); line-height: 1; letter-spacing: 0.2px;
  }
  .header-rule { position: absolute; top: 214px; left: 25px; width: 877px; height: 1px; background: var(--rule-blue); }
  .letter-body {
    position: absolute; top: 254px; left: 59px; width: 809px;
    font-family: Arimo, Arial, sans-serif; font-size: 20px; line-height: 26px; color: var(--ink);
  }
  .letter-body p { margin-bottom: 26px; }
  .line { display: block; white-space: nowrap; text-align: justify; text-align-last: justify; }
  .line.tracked { letter-spacing: 1.6px; }
  .line.end { text-align: left; text-align-last: left; }
  .sign-off {
    position: absolute; top: 836px; right: 59px;
    font-family: Arimo, Arial, sans-serif; font-size: 20px; color: var(--ink); transform: scaleX(0.9); transform-origin: right;
  }
  .signature { position: absolute; top: 880px; left: 748px; width: 112px; height: 38px; background: var(--sig-tone); border-radius: 4px; }
  .footer-wave { position: absolute; left: 0; top: 940px; width: 927px; height: 260px; }
  .contact-list { position: absolute; top: 1012px; left: 0; list-style: none; }
  .contact-item { position: relative; height: 24px; margin-bottom: 12px; }
  .contact-item.address { margin-top: 8px; }
  .contact-pill { position: absolute; left: 0; top: 0; width: 100px; height: 24px; background: #fff; border-radius: 0 12px 12px 0; }
  .contact-pill svg { position: absolute; right: 12px; top: 4px; width: 16px; height: 16px; }
  .contact-text {
    position: absolute; left: 116px; top: 2px; white-space: nowrap;
    font-family: Sarabun, sans-serif; font-weight: 300; font-size: 16px; line-height: 20px; color: var(--footer-text);
  }
</style>
</head>
<body>
<div class="letterhead">
  <div class="top-band"></div>

  <header class="brand">
    <span class="brand-mark"></span>
    <div class="brand-name">Harbor Lumen Capital</div>
  </header>
  <div class="header-rule"></div>

  <main class="letter-body">
    <p>
      <span class="line">Tempor arcu Varius mattis luctus massa, viverra massa vestibulum curae; aliquam</span>
      <span class="line">quisque ante molestie urna vitae magna eros class ultrices. Nam sit nec, nisl</span>
      <span class="line">nonummy urna. Donec hendrerit velit magna vitae amet natoque class quis egestas.</span>
      <span class="line">Ultricies feugiat adipiscing fermentum fames potenti vitae pharetra parturient et vitae</span>
      <span class="line">enim iaculis laoreet turpis sociosqu. Lectus. Pretium nostra primis proin bibendum.</span>
      <span class="line">Amet nisi suscipit curabitur aenean tempor. Quisque hymenaeos dapibus facilisi.</span>
      <span class="line tracked">Curae; fames facilisi bibendum inceptos auctor bibendum nullam.</span>
    </p>
    <p>
      <span class="line">Faucibus ac at Ut consectetuer sem, conubia. Habitant. Dictumst placerat</span>
      <span class="line">laoreet ullamcorper viverra accumsan, hac. Non mauris erat pulvinar nisi</span>
      <span class="line tracked">rutrum tortor odiosodales. Euismod inceptos convallis laoreet</span>
      <span class="line tracked">condimentum erat conubia. Platea class.Suscipit nisi ornare congue.</span>
    </p>
    <p>
      <span class="line">Congue. Amet nonummy integer dictum nostra orci Habitasse porta rhoncus leo justo</span>
      <span class="line">mauris torquent magnis, sociis ornare cursus nec, eu suspendisse risus mollis.</span>
      <span class="line">Consequat ultrices sit Dolor turpis blandit hendrerit ornare per Eros nisl massa.</span>
    </p>
    <p>
      <span class="line">Amet vitae vitae ornare erat dictum per taciti et a hendrerit. Mattis per pellentesque</span>
      <span class="line">vehicula nulla lacus placerat fusce tempor amet primis praesent facilisi ridiculus luctus</span>
      <span class="line">elementum conubia lobortis. Convallis. Nulla curabitur conubia. Ullamcorper curae; erat</span>
      <span class="line">conubia amet auctor rhoncus faucibus. Netus scelerisque. Euismod, amet id pellentesque</span>
      <span class="line end">nam senectus duis magnis quis</span>
    </p>
  </main>

  <div class="sign-off">your sincerely</div>
  <div class="signature" role="img" aria-label="Handwritten signature of the sender"></div>

  <svg class="footer-wave" viewBox="0 0 927 260" aria-hidden="true">
    <path d="M0 38 C70 24 150 16 225 22 C120 22 60 30 0 46 Z" fill="var(--brand-red)"/>
    <path d="M0 52 C110 26 250 20 360 34 C560 58 760 120 927 196 L927 260 L0 260 Z" fill="var(--brand-blue)"/>
    <path d="M360 36 C560 52 760 92 927 102 L927 196 C780 126 580 64 360 36 Z" fill="var(--brand-red)"/>
    <path d="M360 36 C580 62 790 136 927 200 L927 210 C780 140 570 72 360 36 Z" fill="var(--brand-blue)"/>
  </svg>

  <ul class="contact-list">
    <li class="contact-item">
      <span class="contact-pill"><svg viewBox="0 0 16 16"><path d="M3 1 L6 1 L7 5 L5 6.5 C6 9 7.5 10.5 9.5 11 L11 9 L15 10 L15 13 C15 14 14 15 13 15 C6.5 14.5 1.5 9.5 1 3 C1 2 2 1 3 1 Z" fill="var(--brand-red)"/></svg></span>
      <span class="contact-text">01632 960418</span>
    </li>
    <li class="contact-item">
      <span class="contact-pill"><svg viewBox="0 0 16 16"><rect x="1" y="3" width="14" height="10" fill="none" stroke="var(--brand-red)" stroke-width="1.6"/><path d="M1.5 3.5 L8 9 L14.5 3.5" fill="none" stroke="var(--brand-red)" stroke-width="1.6"/></svg></span>
      <span class="contact-text">contact@harborlumencapital.example.co.uk</span>
    </li>
    <li class="contact-item address">
      <span class="contact-pill"><svg viewBox="0 0 16 16"><path d="M8 0.5 C4.8 0.5 2.5 2.8 2.5 5.8 C2.5 9.5 8 15.5 8 15.5 C8 15.5 13.5 9.5 13.5 5.8 C13.5 2.8 11.2 0.5 8 0.5 Z" fill="var(--brand-red)"/><circle cx="8" cy="5.8" r="2" fill="#fff"/></svg></span>
      <span class="contact-text">12-14 Quayside Row<br>Eastbridge<br>Wessex<br>EB2 4QL</span>
    </li>
  </ul>
</div>
</body>
</html>
```